Tovessa Poster

I am looking for a poster to frame for my sister's skin care service business. She treats women of all colors, so i would like a few poster options showing black, white, and latin or asian women.

```html
<!DOCTYPE html>
<html lang="en">
<head>
<meta charset="utf-8">
<title>Tovessa Skin Solutions Poster</title>
<link rel="stylesheet" href="https://fonts.googleapis.com/css2?family=Montserrat:wght@300;400&display=swap">
<style>
  :root {
    --sheet: #ffffff;
    --panel-top: #fdfdfd;
    --panel-bottom: #eeeff1;
    --ink: #2a2a2c;
    --teal: #1fb0a8;
    --teal-deep: #179a93;
    --sky: #d3dfec;
    --skin-light: #ecc3a7;
    --skin-mid: #c98f6c;
    --skin-deep: #6b3f2a;
    --hair-dark: #1e1714;
  }
  * { margin: 0; padding: 0; box-sizing: border-box; }
  html, body {
    width: 921px; height: 1200px; overflow: hidden;
    background: var(--sheet);
  }
  .poster {
    position: relative;
    width: 921px; height: 1200px;
    background: var(--sheet);
    font-family: "Montserrat", sans-serif;
  }
  .poster__panel {
    position: absolute;
    left: 49px; top: 47px;
    width: 823px; height: 1108px;
    background: linear-gradient(180deg, var(--panel-top) 0%, var(--panel-bottom) 100%);
    overflow: hidden;
  }
  .poster__art {
    position: absolute; left: 0; top: 0;
    width: 823px; height: 1108px;
  }
  .badge {
    position: absolute;
    left: 524px; top: 496px;
    width: 244px; height: 244px;
    border-radius: 50%;
    background: var(--sheet);
    border: 8px solid var(--teal);
    display: flex; flex-direction: column;
    align-items: center; justify-content: center;
    gap: 10px;
  }
  .badge__mark {
    width: 18px; height: 18px; border-radius: 50%;
    background: var(--teal);
  }
  .badge__name {
    font-weight: 400;
    font-size: 34px;
    color: var(--teal);
    letter-spacing: 1px;
  }
  .headline {
    position: absolute;
    left: 145px; top: 805px;
    font-weight: 300;
    line-height: 1;
  }
  .headline__lead {
    display: block;
    font-size: 56px;
    color: var(--ink);
    letter-spacing: 1px;
  }
  .headline__mid {
    display: block;
    margin-top: 10px;
    font-size: 76px;
    color: var(--teal);
  }
  .headline__name {
    display: block;
    margin-top: 12px;
    width: 515px; height: 96px;
    background: linear-gradient(90deg, var(--teal) 0%, var(--teal) 80%, var(--teal-deep) 100%);
    color: var(--sheet);
    font-size: 92px;
    line-height: 96px;
    padding-left: 8px;
    white-space: nowrap;
  }
</style>
</head>
<body>
  <main class="poster">
    <div class="poster__panel">
      <svg class="poster__art" viewBox="0 0 823 1108" xmlns="http://www.w3.org/2000/svg">
        <defs>
          <linearGradient id="portraitTones" x1="0" y1="0" x2="1" y2="0">
            <stop offset="0" stop-color="#3a3a3d"/>
            <stop offset="0.28" stop-color="var(--sky)"/>
            <stop offset="0.42" stop-color="var(--skin-light)"/>
            <stop offset="0.62" stop-color="var(--skin-mid)"/>
            <stop offset="0.8" stop-color="var(--skin-deep)"/>
            <stop offset="1" stop-color="var(--hair-dark)"/>
          </linearGradient>
        </defs>
        <path role="img" aria-label="Side profiles of four women with different skin tones, led by a dark grey silhouette profile, facing left against a pale blue backdrop"
              d="M154,0 C60,120 10,300 60,450 C100,560 150,640 152,729 Q600,720 823,389 L823,0 Z"
              fill="url(#portraitTones)"/>
        <path d="M152,731 Q600,722 823,391" fill="none" stroke="var(--teal)" stroke-width="6"/>
      </svg>
      <div class="badge">
        <span class="badge__mark"></span>
        <span class="badge__name">Tovessa</span>
      </div>
    </div>
    <h1 class="headline">
      <span class="headline__lead">HAVE YOUR</span>
      <span class="headline__mid">MOMENT OF</span>
      <span class="headline__name">TOVESSA</span>
    </h1>
  </main>
</body>
</html>
```